Stonebrook 720 Real Estate Investment Company

We need a business card designed for a real estate investment company named Stonebrook 720. We want to use red#f04a50, orange #f37122 and yellow #fbee3e as the color scheme. The logo colors will need to be modified from the current blue palette. I've attach VitaPathway logo example that captures the color scheme we're going for for Stonebrook 720. Looking for clean Sans Serif fonts.
Contact Information for Business Card
Daniel Furlow
Managing Partner
48317 Whitfield Lane, Suite 510
Tampa, FL 33718
813-555-4870 Mobile
dfurlow@stonebrook720.example
www.stonebrook720.example
Requirements
Must have
- Looking for creative responses.
Nice to have
- Must hit color palette... orange, red, yellow

```html
<!DOCTYPE html>
<html lang="en">
<head>
<meta charset="utf-8">
<title>Stonebrook 720 – Business Card</title>
<link href="https://fonts.googleapis.com/css2?family=Lato:wght@300;400;700;900&display=swap" rel="stylesheet">
<style>
  :root {
    --bg: #dcdcdc;
    --card: #111111;
    --red: #f04a50;
    --orange: #f37122;
    --yellow: #fbee3e;
    --text: #d8d8d8;
    --muted: #a9a9a9;
    --rule: #2a2a2a;
  }
  html, body {
    margin: 0;
    width: 1200px;
    height: 782px;
    overflow: hidden;
    background: var(--bg);
    font-family: "Lato", Arial, sans-serif;
  }
  .card {
    position: absolute;
    top: 236px;
    width: 540px;
    height: 309px;
    background: var(--card);
    box-shadow: 0 10px 24px rgba(0,0,0,0.25);
    overflow: hidden;
  }
  .card--front { left: 40px; }
  .card--back { left: 620px; }

  .brand {
    position: absolute;
    display: flex;
    align-items: center;
    gap: 10px;
    color: var(--yellow);
    font-weight: 900;
    font-size: 27px;
    letter-spacing: 0.2px;
    white-space: nowrap;
  }
  .brand__dot {
    width: 14px;
    height: 14px;
    border-radius: 50%;
    background: var(--orange);
  }
  .card--front .brand { left: 180px; top: 128px; }
  .card--back .brand { right: 44px; top: 56px; }

  .stripe {
    position: absolute;
    left: 0; right: 0; bottom: 0;
    height: 6px;
    display: flex;
  }
  .stripe span { flex: 1; }
  .stripe .s-orange { background: var(--orange); }
  .stripe .s-red { background: var(--red); }
  .stripe .s-yellow { background: var(--yellow); }

  .person {
    position: absolute;
    left: 30px;
    top: 108px;
  }
  .person__name {
    margin: 0;
    color: var(--orange);
    font-weight: 700;
    font-size: 21px;
    line-height: 1.1;
  }
  .person__title {
    margin: 2px 0 8px;
    color: var(--muted);
    font-weight: 400;
    font-size: 13px;
  }
  .contact {
    list-style: none;
    margin: 0;
    padding: 0;
    color: var(--text);
    font-size: 14px;
    line-height: 21px;
  }
  .contact li { display: flex; align-items: center; gap: 8px; }
  .contact svg { width: 12px; height: 12px; fill: var(--orange); flex: none; overflow: visible; }

  .rule {
    position: absolute;
    left: 30px;
    right: 44px;
    top: 234px;
    height: 1px;
    background: var(--rule);
  }
  .address {
    position: absolute;
    right: 44px;
    top: 244px;
    margin: 0;
    text-align: right;
    color: var(--text);
    font-style: normal;
    font-size: 15px;
    line-height: 20px;
  }
</style>
</head>
<body>

<section class="card card--front" aria-label="Card front">
  <div class="brand"><span class="brand__name">Stonebrook 720</span><span class="brand__dot"></span></div>
  <div class="stripe"><span class="s-orange"></span><span class="s-red"></span><span class="s-yellow"></span></div>
</section>

<section class="card card--back" aria-label="Card back">
  <div class="brand"><span class="brand__name">Stonebrook 720</span><span class="brand__dot"></span></div>

  <div class="person">
    <h1 class="person__name">Daniel Furlow</h1>
    <p class="person__title">Managing Partner</p>
    <ul class="contact">
      <li>
        <svg viewBox="0 0 12 12" aria-hidden="true"><path d="M2.4 0.6l2 2.2-1 1.4c.7 1.6 1.8 2.7 3.4 3.4l1.4-1 2.2 2-1 2.2C5 10.6 1.4 7 .6 1.6z"/></svg>
        <span>813-555-4870</span>
      </li>
      <li>
        <svg viewBox="0 0 12 12" aria-hidden="true"><path d="M0 2h12v8H0z M1 3l5 3.5L11 3v-.2H1z" fill-rule="evenodd"/></svg>
        <span>dfurlow@stonebrook720.example</span>
      </li>
      <li>
        <svg viewBox="0 0 12 12" aria-hidden="true">
          <circle cx="6" cy="6" r="5.5"/>
          <path d="M0.5 6h11M6 0.5c-2 2-2 9 0 11M6 0.5c2 2 2 9 0 11" fill="none" stroke="#111111" stroke-width="0.8"/>
        </svg>
        <span>www.stonebrook720.example</span>
      </li>
    </ul>
  </div>

  <div class="rule"></div>

  <address class="address">48317 Whitfield Lane<br>Suite 510 Tampa, FL 33718</address>

  <div class="stripe"><span class="s-orange"></span><span class="s-red"></span><span class="s-yellow"></span></div>
</section>

</body>
</html>
```